Modern SaaS Dashboard Redesign for Building Management Platform

Overview:
Refer to pelvorn.com.au
We need a complete visual redesign of our property management dashboard to make it sleek, modern, and highly user-friendly. The current interface is functional but outdated. We want a high end SaaS design that feels intuitive, and visually engaging for daily use.

Style Direction:

Retain existing colour palette
Consistent, modern iconography and typography
Responsive design consideration (desktop-first, but adaptable to mobile)

Deliverables:
High-fidelity dashboard design in Figma or Adobe XD
Style guide for colours, typography, and icons
Layered files for developer handoff

Customer Journey Context

This dashboard is the central control panel for a property management SaaS platform (Pelvorn) used by building managers, strata managers, and executive committee members to manage building data and operations.

Entry Point: User logs in via the secure portal → lands directly on the dashboard.

Primary Goal: Quickly assess building portfolio health, upcoming actions, and key compliance dates.

Secondary Goal: Navigate smoothly to specific building data, reports, or contractor tasks without getting lost in menus.

Typical Flow:

Glance Phase (0–10 seconds) – User scans top stat cards for red/orange alerts or overdue actions.

Action Phase (10–30 seconds) – Clicks into urgent items from “Next Action List” or stat cards.

Work Phase (1–5 minutes) – Navigates to buildings or reports for detail work, filters/searches, and updates records.

2. Who This is For

Building Managers – Daily operational users, need fast visibility of inspections, insurance, defects, and maintenance.

Strata Managers / Property Managers – Portfolio-level oversight across multiple buildings.

Executive Committee Members (Owners Corporations) – View-only or limited-action users needing transparency and governance oversight.

Internal Support/Admin Staff – Back-office users providing data entry, compliance tracking, and troubleshooting.

3. Stakeholders Who Will See This Dashboard

Internal Admin Team – To monitor user activity and portfolio health.

Portfolio Managers – To track multiple properties at once and ensure compliance deadlines aren’t missed.

Building Service Providers – Certain contractors may have limited dashboard visibility for their assigned properties.

Compliance Officers / Auditors – May access the dashboard to verify documentation and timelines.

4. Key Design Considerations Based on Audience

Immediate clarity – Visual hierarchy that prioritises critical actions first.

Minimal learning curve – Clean, intuitive navigation with consistent patterns.

Quick search/filtering – Users may have dozens or hundreds of buildings to manage.

Mobile awareness – Many building managers work in the field, so components should adapt for tablets and smaller screens.

```html
<!DOCTYPE html>
<html lang="en">
<head>
<meta charset="utf-8">
<title>Pelvorn Dashboard – Design Variations</title>
<link href="https://fonts.googleapis.com/css2?family=Montserrat:wght@700;800&family=Poppins:wght@400;500;600;700&display=swap" rel="stylesheet">
<style>
:root{
  --stage:#6e6e6e;
  --indigo:#4a4585;
  --indigo-dark:#3f3d72;
  --ink:#3b3a5c;
  --muted:#7b7b8e;
  --line:#e6e3ef;
  --field:#ffffff;
  --green:#2f9f73;
  --orange:#ee8a4f;
  --red:#e2475c;
  --glass:rgba(255,255,255,.5);
  --glass-edge:rgba(255,255,255,.75);
}
*{box-sizing:border-box;margin:0;padding:0}
html,body{width:1200px;height:3000px;overflow:hidden}
body{background:var(--stage);font-family:'Poppins',sans-serif;color:var(--ink);position:relative}
.variation-title{position:absolute;left:0;width:1200px;text-align:center;font-family:'Montserrat',sans-serif;font-weight:800;font-size:27px;letter-spacing:1.5px;color:#fff}
.board{position:absolute;width:882px;background:linear-gradient(135deg,#eeedfb 0%,#f4eefa 40%,#f9eef7 70%,#fbf4ea 100%);overflow:hidden}
.board--one{left:163px;top:98px;height:1355px}
.board--two{left:158px;top:1549px;height:1400px}
.footer{position:absolute;left:0;right:0;bottom:0;height:28px;background:var(--indigo);color:#fff;font-size:9px;display:flex;align-items:center;justify-content:center}

/* sidebar */
.sidebar{position:absolute;left:20px;top:15px;width:198px;height:400px;background:rgba(255,255,255,.35);border:1px solid var(--glass-edge);border-radius:8px;padding:14px 12px}
.brand{display:flex;align-items:center;gap:8px;height:48px;padding-left:4px;border-bottom:1px solid var(--line)}
.brand__dot{width:22px;height:22px;border-radius:50%;background:var(--indigo-dark)}
.brand__name{font-weight:700;font-size:15px;color:var(--indigo-dark);letter-spacing:.5px}
.nav{list-style:none;margin-top:22px}
.nav__item{display:flex;align-items:center;gap:9px;height:37px;padding:0 9px;font-size:9.5px;color:#55556a}
.nav__item svg{width:13px;height:13px;fill:none;stroke:#8a8aa0;stroke-width:1.5}
.nav__item--active{background:var(--indigo);color:#fff;border-radius:4px;font-weight:600;height:36px;margin-bottom:1px}
.nav__item--active svg{stroke:#fff}
.nav__chev{margin-left:auto;margin-right:20px}

/* main */
.main{position:absolute;left:234px;top:15px;width:628px}
.topbar{height:47px;background:var(--glass);border:1px solid var(--glass-edge);border-radius:8px;display:flex;align-items:center;padding:0 14px}
.topbar__title{font-size:15.5px;font-weight:600;color:var(--indigo-dark)}
.theme{margin-left:auto;display:flex;align-items:center;gap:8px;padding-right:14px;border-right:1px solid var(--line);height:26px}
.theme svg{width:13px;height:13px;fill:none;stroke:#555;stroke-width:1.4}
.toggle{width:24px;height:10px;border-radius:5px;background:#dcdbe8;position:relative}
.toggle::before{content:"";position:absolute;left:0;top:-1px;width:12px;height:12px;border-radius:50%;background:var(--indigo)}
.company{font-size:10px;font-weight:600;color:var(--indigo-dark);margin:0 10px 0 16px}
.company-badge{width:36px;height:36px;border-radius:50%;background:var(--indigo);border:3px solid #cfcbe6;color:#fff;font-size:10px;font-weight:700;line-height:10px;display:flex;align-items:center;justify-content:center;text-align:center}
.userbar{margin-top:16px;height:36px;background:var(--glass);border:1px solid var(--glass-edge);border-radius:8px;display:flex;align-items:center;padding:0 12px;gap:8px}
.gear{width:20px;height:20px;border-radius:50%;border:1px solid #ccc;display:flex;align-items:center;justify-content:center}
.gear svg{width:11px;height:11px;fill:none;stroke:#999;stroke-width:1.5}
.avatar{width:22px;height:22px;border-radius:50%;background:radial-gradient(circle at 50% 40%,#f2b487,#c26a3c)}
.user__name{font-size:10px;font-weight:600;color:var(--ink);line-height:12px}
.user__mail{font-size:8px;color:var(--muted)}
.user__icons{display:flex;gap:10px;margin-left:32px}
.user__icons svg{width:13px;height:13px;fill:none;stroke:#666;stroke-width:1.4}
.board--two .user__icons{margin-left:auto}

/* stats */
.stats{display:grid;margin-top:22px;gap:15px 14px}
.board--one .stats{grid-template-columns:129px 129px 129px 199px;grid-template-rows:90px 90px}
.board--two .stats{margin-top:16px;grid-template-columns:129px 129px 129px 199px;grid-template-rows:90px 90px;row-gap:14px}
.stat{position:relative;border-radius:8px;color:#fff;padding:14px 8px;overflow:hidden;box-shadow:0 4px 10px rgba(90,60,120,.15)}
.stat::before{content:"";position:absolute;left:-20px;top:-30px;width:90px;height:90px;border-radius:50%;background:rgba(255,255,255,.12)}
.stat__num{display:block;font-size:26px;font-weight:700;line-height:28px;position:relative}
.stat__label{display:block;font-size:8.5px;font-weight:600;line-height:11px;margin-top:4px;position:relative}
.stat__label--small{font-size:7.5px;line-height:9.5px}
.stat__icon{position:absolute;right:10px;bottom:14px;width:32px;height:32px;fill:none;stroke:#fff;stroke-width:1.4;opacity:.9}
.stat--portfolio{background:linear-gradient(135deg,#d24a7b,#6f4b88)}
.stat--actions{background:linear-gradient(135deg,#d8447b,#ee8a78)}
.stat--inspections{background:linear-gradient(135deg,#df5a70,#eca46a)}
.stat--insurance{background:linear-gradient(135deg,#e2497b,#ef9289)}
.stat--defects{background:linear-gradient(135deg,#e0527d,#eda26b)}
.stat--maintenance{background:linear-gradient(45deg,#d6567e,#5c4886)}

.overview-pie{grid-column:4;grid-row:1 / span 2;background:rgba(255,255,255,.85);border-radius:8px;padding:28px 16px;position:relative;box-shadow:0 4px 12px rgba(90,60,120,.08)}
.overview-pie__title{font-size:15px;color:#5a5a72;font-weight:500}
.overview-pie svg{position:absolute;left:14px;top:62px;width:115px;height:115px}
.legend{position:absolute;left:140px;top:98px;list-style:none;font-size:6.5px;color:#555;line-height:15px}
.legend span{display:inline-block;width:4px;height:4px;border-radius:50%;margin-right:5px;vertical-align:middle}

/* calendar */
.calendar{background:rgba(255,255,255,.6);border-radius:6px;overflow:hidden;border:1px solid var(--glass-edge)}
.calendar__head{height:24px;background:var(--indigo);color:#fff;font-size:7.5px;font-weight:500;display:flex;align-items:center;justify-content:space-between;padding:0 10px}
.calendar__head i{width:11px;height:11px;border-radius:50%;background:#fff;display:inline-block;position:relative}
.calendar__head i::after{content:"";position:absolute;left:3.5px;top:4px;width:3px;height:3px;border-left:1.2px solid var(--indigo);border-top:1.2px solid var(--indigo);transform:rotate(45deg)}
.calendar__month{text-align:center;font-size:8.5px;font-weight:600;margin:12px 0 14px}
.calendar__grid{display:grid;grid-template-columns:repeat(7,1fr);padding:0 6px;text-align:center;font-size:7.5px;row-gap:6px}
.calendar__grid b{font-size:5.5px;font-weight:700;color:#333;margin-bottom:2px}
.calendar__grid .today{background:#e07f53;color:#fff;border-radius:50%;width:14px;height:14px;line-height:14px;margin:-2px auto 0}

/* next actions */
.actions{background:rgba(255,255,255,.4);border:1px solid var(--glass-edge);border-radius:8px;padding:14px}
.actions__title{display:flex;align-items:center;gap:8px;font-size:10px;font-weight:500}
.actions__title svg{width:14px;height:14px;fill:none;stroke:var(--green);stroke-width:1.6}
.select{height:22px;border:1px solid #cfcbe0;background:#fff;border-radius:3px;font-size:9px;padding:0 8px;display:flex;align-items:center;justify-content:space-between;color:var(--ink)}
.select::after{content:"";width:4px;height:4px;border-right:1px solid #666;border-bottom:1px solid #666;transform:rotate(45deg);margin-top:-3px}
.action__date{color:var(--green);font-size:10.5px;font-weight:500}
.action__text{font-size:7px;color:#666;line-height:11px;margin-top:3px}
.btn-more{display:block;width:50px;height:23px;margin:0 auto;border:1px solid #9c98c2;border-radius:4px;background:#fff;font-size:9.5px;text-align:center;line-height:21px;color:#55557a}

.board--one .row-two{display:grid;grid-template-columns:199px 415px;gap:14px;margin-top:20px;height:177px}
.board--one .actions__top{display:flex;align-items:center;margin-top:8px}
.board--one .actions__top .select{width:185px}
.arrows{margin-left:auto;display:flex;gap:16px;font-size:14px;color:#444}
.action-cols{display:grid;grid-template-columns:repeat(3,1fr);gap:12px;margin:12px 0 16px}

.board--two .stats .calendar{grid-column:4;grid-row:1 / span 2}
.board--two .row-two{display:grid;grid-template-columns:415px 199px;gap:14px;margin-top:15px;height:234px}
.chart{background:rgba(255,255,255,.55);border-radius:8px;padding:12px 6px;position:relative;box-shadow:0 6px 12px rgba(110,90,200,.18)}
.chart__title{font-size:9.5px;font-weight:500;padding-left:1px}
.chart__range{position:absolute;right:22px;top:12px;width:72px;height:17px;border:1px solid #ccc;border-radius:3px;background:#fff;font-size:6.5px;color:#999;padding:0 6px;display:flex;align-items:center;justify-content:space-between}
.chart__range::after{content:"";width:3px;height:3px;border-right:1px solid #555;border-bottom:1px solid #555;transform:rotate(45deg)}
.chart svg{position:absolute;left:6px;top:40px;width:400px;height:185px}
.board--two .actions{padding:12px}
.board--two .actions .select{margin-top:10px}
.action-list .action__date{margin-top:10px;font-size:10px}
.board--two .btn-more{margin-top:12px}

/* filter */
.filter{margin-top:16px;height:157px;background:rgba(255,255,255,.4);border:1px solid var(--glass-edge);border-radius:8px;overflow:hidden}
.filter__head{height:43px;display:flex;align-items:center;padding:0 8px}
.filter__title{font-size:15px;font-weight:600;color:var(--indigo-dark)}
.btn{height:24px;border-radius:12px;font-size:8px;padding:0 12px;display:flex;align-items:center}
.btn--primary{background:var(--indigo);color:#fff;margin-left:auto}
.btn--outline{border:1px solid var(--indigo);color:var(--indigo);margin-left:14px;background:#fff}
.collapse{width:14px;height:2px;background:var(--indigo);margin:0 4px 0 14px}
.filter__body{background:rgba(255,255,255,.75);height:114px;display:grid;grid-template-columns:repeat(4,135px);column-gap:15px;padding:10px 7px 0;row-gap:6px}
.field label{display:block;font-size:6.5px;font-weight:600;margin-bottom:6px}
.field .input,.field .select{height:23px;border:1px solid #c9c6d8;border-radius:2px;background:#fff;font-size:6.5px;color:#999;padding:0 6px;display:flex;align-items:center}

/* table */
.buildings{margin-top:15px;height:572px;background:rgba(255,255,255,.8);border-radius:8px;overflow:hidden}
table{width:100%;border-collapse:collapse;table-layout:fixed}
thead th{background:var(--indigo);color:#fff;font-size:8.5px;font-weight:500;height:37px;line-height:10px;text-align:left;padding:0 4px}
thead th.c{text-align:center}
tbody td{font-size:7px;color:#666;height:24px;border-bottom:1px solid #ebe8f1;padding:0 4px;white-space:nowrap;overflow:hidden}
tbody td:first-child{padding-left:18px}
td.num{text-align:center}
td.act{text-align:center}
.ic{display:inline-block;width:9px;height:9px;border:1px solid;border-radius:2px;margin:0 2px;font-style:normal;font-size:6px;line-height:7px;text-align:center;vertical-align:middle}
.ic.e{border-color:var(--orange);color:var(--orange)}
.ic.e::after{content:"✎"}
.ic.c{border-color:var(--green);color:var(--green)}
.ic.c::after{content:"✓"}
.ic.x{border-color:var(--red);color:var(--red);border-radius:50%}
.ic.x::after{content:"×"}
.pager{display:flex;align-items:center;justify-content:center;gap:10px;margin-top:21px;font-size:8px}
.pager__btn{height:21px;border:1px solid #e2e0ea;border-radius:3px;padding:0 10px;display:flex;align-items:center;background:#fff}
.pager__btn--off{color:#c6c6cf}
.pager__page{width:19px;height:21px;border-radius:3px;background:var(--indigo);color:#fff;display:flex;align-items:center;justify-content:center}
.pager__label{font-weight:600;margin-left:6px}
.pager__size{width:38px;height:21px;border:1px solid #e2e0ea;border-radius:3px;background:#fff;display:flex;align-items:center;justify-content:space-around;padding:0 4px}
.pager__count{margin-left:10px}
</style>
</head>
<body>

<h1 class="variation-title" style="top:24px">DESIGN VARIATION 01</h1>

<section class="board board--one">
  <aside class="sidebar">
    <div class="brand"><span class="brand__dot"></span><span class="brand__name">PELVORN</span></div>
    <ul class="nav">
      <li class="nav__item nav__item--active"><svg viewBox="0 0 14 14"><path d="M2 7 7 2l5 5M3.5 6v6h7V6M6 12V9h2v3"/></svg>Buildings</li>
      <li class="nav__item"><svg viewBox="0 0 14 14"><path d="M1 3h5v9H1zM8 3h5v9H8z"/></svg>Contractors Address Book</li>
      <li class="nav__item"><svg viewBox="0 0 14 14"><path d="M3 1h8v12H3zM5 4h4M5 7h4M5 10h2"/></svg>Report Builder</li>
      <li class="nav__item"><svg viewBox="0 0 14 14"><ellipse cx="7" cy="3" rx="5" ry="2"/><path d="M2 3v8c0 1 2 2 5 2s5-1 5-2V3M2 7c0 1 2 2 5 2s5-1 5-2"/></svg>Management Data</li>
      <li class="nav__item"><svg viewBox="0 0 14 14"><path d="M1 3h12v9H1zM1 3l6 5 6-5"/></svg>Email Log Report</li>
      <li class="nav__item"><svg viewBox="0 0 14 14"><ellipse cx="7" cy="3" rx="5" ry="2"/><path d="M2 3v8c0 1 2 2 5 2s5-1 5-2V3"/></svg>&nbsp;&nbsp;&nbsp;Administration<svg class="nav__chev" viewBox="0 0 14 14"><path d="M3 5l4 4 4-4"/></svg></li>
      <li class="nav__item"><svg viewBox="0 0 14 14"><circle cx="6" cy="4" r="2.5"/><path d="M1 13c0-3 2-5 5-5M9 10l1.5 1.5L13 9"/></svg>About Us + Support</li>
      <li class="nav__item"><svg viewBox="0 0 14 14"><path d="M1 3h5v9H1zM8 3h5v9H8z"/></svg>Training Hub</li>
    </ul>
  </aside>

  <main class="main">
    <header class="topbar">
      <h2 class="topbar__title">Dashboard</h2>
      <div class="theme">
        <svg viewBox="0 0 14 14"><circle cx="7" cy="7" r="2.5"/><path d="M7 1v2M7 11v2M1 7h2M11 7h2M2.8 2.8l1.4 1.4M9.8 9.8l1.4 1.4M2.8 11.2l1.4-1.4M9.8 4.2l1.4-1.4"/></svg>
        <span class="toggle"></span>
        <svg viewBox="0 0 14 14"><path d="M11 9A5 5 0 0 1 5 3a5 5 0 1 0 6 6z"/></svg>
      </div>
      <span class="company">USER COMPANY LOGO</span>
      <span class="company-badge">LO<br>GO</span>
    </header>

    <div class="userbar">
      <span class="gear"><svg viewBox="0 0 12 12"><circle cx="6" cy="6" r="2"/><circle cx="6" cy="6" r="4.5" stroke-dasharray="2 1.5"/></svg></span>
      <span class="avatar" role="img" aria-label="User profile photo"></span>
      <div><div class="user__name">PELVORN</div><div class="user__mail">admininfo@postmail.com</div></div>
      <div class="user__icons">
        <svg viewBox="0 0 14 14"><path d="M3 10V6a4 4 0 0 1 8 0v4l1 1H2zM6 13h2"/></svg>
        <svg viewBox="0 0 14 14"><path d="M1 3h12v8H1zM1 3l6 5 6-5"/></svg>
      </div>
    </div>

    <div class="stats">
      <div class="stat stat--portfolio"><span class="stat__num">8</span><span class="stat__label">Building in This<br>Portfolio</span><svg class="stat__icon" viewBox="0 0 32 32"><path d="M4 30V10h10v20M14 30V4h12v26M2 30h28M7 14h4M7 18h4M7 22h4M17 8h6M17 12h6M17 16h6M17 20h6M17 24h6"/></svg></div>
      <div class="stat stat--actions"><span class="stat__num">10</span><span class="stat__label">Today's Next<br>Actions</span><svg class="stat__icon" viewBox="0 0 32 32"><path d="M24 18v10H4V10h8M20 4h8v8M28 4 16 16"/></svg></div>
      <div class="stat stat--inspections"><span class="stat__num">10</span><span class="stat__label stat__label--small">Upcoming<br>Inspections/ Expiring<br>Contracts</span><svg class="stat__icon" viewBox="0 0 32 32"><path d="M3 6h26v22H3zM3 12h26M9 3v6M23 3v6M8 17h3M14 17h3M20 17h3M8 22h3M14 22h3M20 22h3"/></svg></div>
      <div class="overview-pie">
        <h3 class="overview-pie__title">Overview</h3>
        <svg viewBox="0 0 100 100">
          <circle cx="50" cy="50" r="25" fill="none" stroke="#5f86d3" stroke-width="50" stroke-dasharray="94 157" transform="rotate(-90 50 50)"/>
          <circle cx="50" cy="50" r="25" fill="none" stroke="#f2cc3c" stroke-width="50" stroke-dasharray="0 94 40 157" transform="rotate(-90 50 50)"/>
          <circle cx="50" cy="50" r="25" fill="none" stroke="#ec6e76" stroke-width="50" stroke-dasharray="0 134 23 157" transform="rotate(-90 50 50)"/>
          <text x="64" y="66" font-size="7" fill="#fff" font-family="Poppins">75%</text>
          <text x="10" y="48" font-size="7" fill="#fff" font-family="Poppins">27%</text>
          <text x="28" y="22" font-size="7" fill="#fff" font-family="Poppins">16%</text>
        </svg>
        <ul class="legend">
          <li><span style="background:#5f86d3"></span>Blue</li>
          <li><span style="background:#f2cc3c"></span>Yellow</li>
          <li><span style="background:#ec6e76"></span>Red</li>
        </ul>
      </div>
      <div class="stat stat--insurance"><span class="stat__num">10</span><span class="stat__label">Insurance Pending<br>or Overview</span><svg class="stat__icon" viewBox="0 0 32 32"><path d="M3 16a13 13 0 0 1 26 0zM16 16v10a3 3 0 0 1-6 0M16 3v2"/></svg></div>
      <div class="stat stat--defects"><span class="stat__num">10</span><span class="stat__label stat__label--small">Defects Register\<br>Feedback Requested</span><svg class="stat__icon" viewBox="0 0 32 32"><path d="M24 16v12H4V6h14M8 12h8M8 17h8M8 22h6M28 6 18 18l-3 1 1-3L26 4z"/></svg></div>
      <div class="stat stat--maintenance"><span class="stat__num">8</span><span class="stat__label">Open Maintenance<br>Requests</span><svg class="stat__icon" viewBox="0 0 32 32"><circle cx="18" cy="11" r="4"/><circle cx="18" cy="11" r="8" stroke-dasharray="3 2"/><path d="M2 24h6l6 3 10-4M8 24l5-4h5"/></svg></div>
    </div>

    <div class="row-two">
      <div class="calendar">
        <div class="calendar__head"><span>Select Your Date &amp; Time</span><i></i></div>
        <div class="calendar__month">‹&nbsp;&nbsp;September 2025&nbsp;&nbsp;›</div>
        <div class="calendar__grid">
          <b>SUN</b><b>MON</b><b>TUE</b><b>WED</b><b>THU</b><b>FRI</b><b>SAT</b>
          <span>28</span><span>29</span><span>30</span><span>1</span><span>2</span><span>3</span><span>4</span>
          <span>5</span><span>6</span><span>7</span><span>8</span><span>9</span><span>10</span><span>11</span>
          <span>12</span><span>13</span><span>14</span><span>15</span><span>16</span><span>17</span><span>18</span>
          <span>19</span><span>20</span><span class="today">21</span><span>22</span><span>23</span><span>24</span><span>25</span>
          <span>26</span><span>27</span><span>28</span><span>29</span><span>30</span><span>31</span><span>1</span>
        </div>
      </div>
      <div class="actions">
        <div class="actions__title"><svg viewBox="0 0 14 14"><path d="M12 7v6H1V2h8M4 6l3 3 6-7"/></svg>Next Action List</div>
        <div class="actions__top"><div class="select">Pelvorn</div><div class="arrows"><span>‹</span><span>›</span></div></div>
        <div class="action-cols">
          <div><div class="action__date">22 August, 2025</div><p class="action__text">Streamline building engagement. Immediate access to data. New Buildings.</p></div>
          <div><div class="action__date">22 August, 2025</div><p class="action__text">Streamline building engagement. Immediate access to data. New Buildings.</p></div>
          <div><div class="action__date">22 August, 2025</div><p class="action__text">Streamline building engagement. Immediate access to data. New Buildings.</p></div>
        </div>
        <span class="btn-more">More</span>
      </div>
    </div>

    <section class="filter">
      <div class="filter__head">
        <h3 class="filter__title">Buildings Filter</h3>
        <span class="btn btn--primary">+Add New</span>
        <span class="btn btn--outline">Export to Excel</span>
        <span class="collapse"></span>
      </div>
      <div class="filter__body">
        <div class="field"><label>Units Plan No.</label><div class="input">Units Plan No.</div></div>
        <div class="field"><label>Building Name</label><div class="input">Building name</div></div>
        <div class="field"><label>Street Name</label><div class="input">Street name</div></div>
        <div class="field"><label>Street No.</label><div class="input">Street No.</div></div>
        <div class="field"><label>Suburb</label><div class="select">Select--</div></div>
        <div class="field"><label>Group</label><div class="select">Select--</div></div>
        <div class="field"><label>Builder</label><div class="input">Builder</div></div>
        <div class="field"><label>Building Status</label><div class="select">Active</div></div>
      </div>
    </section>

    <section class="buildings">
      <table>
        <colgroup><col style="width:45px"><col style="width:76px"><col style="width:79px"><col style="width:72px"><col style="width:79px"><col style="width:52px"><col style="width:55px"><col style="width:111px"><col></colgroup>
        <thead><tr><th class="c">S.No.</th><th>Units Plan No.</th><th>Building Name</th><th>Group Name</th><th class="c">Street<br>Number &amp; Name</th><th>Suburb</th><th>Live Posts</th><th class="c">Pelvorn Subscriptions<br>Renewal</th><th class="c">Action</th></tr></thead>
        <tbody>
          <tr><td>01.</td><td>000884</td><td>Building Name</td><td>Harlow Brennan</td><td>41 Tallow Street</td><td>Merridale</td><td>00</td><td class="num">09-May-2026</td><td class="act"><i class="ic e"></i><i class="ic c"></i><i class="ic x"></i></td></tr>
          <tr><td>02.</td><td>000884</td><td>Building Name</td><td>Harlow Brennan</td><td>41 Tallow Street</td><td>Merridale</td><td>00</td><td class="num">09-May-2026</td><td class="act"><i class="ic e"></i><i class="ic c"></i><i class="ic x"></i></td></tr>
          <tr><td>03.</td><td>000884</td><td>Building Name</td><td>Harlow Brennan</td><td>41 Tallow Street</td><td>Merridale</td><td>00</td><td class="num">09-May-2026</td><td class="act"><i class="ic e"></i><i class="ic c"></i><i class="ic x"></i></td></tr>
          <tr><td>04.</td><td>000884</td><td>Building Name</td><td>Harlow Brennan</td><td>41 Tallow Street</td><td>Merridale</td><td>00</td><td class="num">09-May-2026</td><td class="act"><i class="ic e"></i><i class="ic c"></i><i class="ic x"></i></td></tr>
          <tr><td>05.</td><td>000884</td><td>Building Name</td><td>Harlow Brennan</td><td>41 Tallow Street</td><td>Merridale</td><td>00</td><td class="num">09-May-2026</td><td class="act"><i class="ic e"></i><i class="ic c"></i><i class="ic x"></i></td></tr>
          <tr><td>06.</td><td>000884</td><td>Building Name</td><td>Harlow Brennan</td><td>41 Tallow Street</td><td>Merridale</td><td>00</td><td class="num">09-May-2026</td><td class="act"><i class="ic e"></i><i class="ic c"></i><i class="ic x"></i></td></tr>
          <tr><td>07.</td><td>000884</td><td>Building Name</td><td>Harlow Brennan</td><td>41 Tallow Street</td><td>Merridale</td><td>00</td><td class="num">09-May-2026</td><td class="act"><i class="ic e"></i><i class="ic c"></i><i class="ic x"></i></td></tr>
          <tr><td>08.</td><td>000884</td><td>Building Name</td><td>Harlow Brennan</td><td>41 Tallow Street</td><td>Merridale</td><td>00</td><td class="num">09-May-2026</td><td class="act"><i class="ic e"></i><i class="ic c"></i><i class="ic x"></i></td></tr>
          <tr><td>09.</td><td>000884</td><td>Building Name</td><td>Harlow Brennan</td><td>41 Tallow Street</td><td>Merridale</td><td>00</td><td class="num">09-May-2026</td><td class="act"><i class="ic e"></i><i class="ic c"></i><i class="ic x"></i></td></tr>
          <tr><td>10.</td><td>000884</td><td>Building Name</td><td>Harlow Brennan</td><td>41 Tallow Street</td><td>Merridale</td><td>00</td><td class="num">09-May-2026</td><td class="act"><i class="ic e"></i><i class="ic c"></i><i class="ic x"></i></td></tr>
          <tr><td>11.</td><td>000884</td><td>Building Name</td><td>Harlow Brennan</td><td>41 Tallow Street</td><td>Merridale</td><td>00</td><td class="num">09-May-2026</td><td class="act"><i class="ic e"></i><i class="ic c"></i><i class="ic x"></i></td></tr>
          <tr><td>12.</td><td>000884</td><td>Building Name</td><td>Harlow Brennan</td><td>41 Tallow Street</td><td>Merridale</td><td>00</td><td class="num">09-May-2026</td><td class="act"><i class="ic e"></i><i class="ic c"></i><i class="ic x"></i></td></tr>
          <tr><td>13</td><td>000884</td><td>Building Name</td><td>Harlow Brennan</td><td>41 Tallow Street</td><td>Merridale</td><td>00</td><td class="num">09-May-2026</td><td class="act"><i class="ic e"></i><i class="ic c"></i><i class="ic x"></i></td></tr>
          <tr><td>14.</td><td>000884</td><td>Building Name</td><td>Harlow Brennan</td><td>41 Tallow Street</td><td>Merridale</td><td>00</td><td class="num">09-May-2026</td><td class="act"><i class="ic e"></i><i class="ic c"></i><i class="ic x"></i></td></tr>
          <tr><td>15.</td><td>000884</td><td>Building Name</td><td>Harlow Brennan</td><td>41 Tallow Street</td><td>Merridale</td><td>00</td><td class="num">09-May-2026</td><td class="act"><i class="ic e"></i><i class="ic c"></i><i class="ic x"></i></td></tr>
          <tr><td>16.</td><td>000884</td><td>Building Name</td><td>Harlow Brennan</td><td>41 Tallow Street</td><td>Merridale</td><td>00</td><td class="num">09-May-2026</td><td class="act"><i class="ic e"></i><i class="ic c"></i><i class="ic x"></i></td></tr>
          <tr><td>17.</td><td>000884</td><td>Building Name</td><td>Harlow Brennan</td><td>41 Tallow Street</td><td>Merridale</td><td>00</td><td class="num">09-May-2026</td><td class="act"><i class="ic e"></i><i class="ic c"></i><i class="ic x"></i></td></tr>
          <tr><td>18.</td><td>000884</td><td>Building Name</td><td>Harlow Brennan</td><td>41 Tallow Street</td><td>Merridale</td><td>00</td><td class="num">09-May-2026</td><td class="act"><i class="ic e"></i><i class="ic c"></i><i class="ic x"></i></td></tr>
          <tr><td>19.</td><td>000884</td><td>Building Name</td><td>Harlow Brennan</td><td>41 Tallow Street</td><td>Merridale</td><td>00</td><td class="num">09-May-2026</td><td class="act"><i class="ic e"></i><i class="ic c"></i><i class="ic x"></i></td></tr>
          <tr><td>20.</td><td>000884</td><td>Building Name</td><td>Harlow Brennan</td><td>41 Tallow Street</td><td>Merridale</td><td>00</td><td class="num">09-May-2026</td><td class="act"><i class="ic e"></i><i class="ic c"></i><i class="ic x"></i></td></tr>
        </tbody>
      </table>
      <div class="pager">
        <span class="pager__btn pager__btn--off">‹&nbsp; Back</span><span class="pager__page">1</span><span class="pager__btn">Next &nbsp;›</span>
        <span class="pager__label">Result per page</span><span class="pager__size">20 <small>⌄</small></span><span class="pager__count">1-20 of 100</span>
      </div>
    </section>
  </main>

  <footer class="footer">Copyright © 2025 Pelvorn | All Rights Reserved | Privacy Policy</footer>
</section>

<h1 class="variation-title" style="top:1482px">DESIGN VARIATION 02</h1>

<section class="board board--two">
  <aside class="sidebar">
    <div class="brand"><span class="brand__dot"></span><span class="brand__name">PELVORN</span></div>
    <ul class="nav">
      <li class="nav__item nav__item--active"><svg viewBox="0 0 14 14"><path d="M2 7 7 2l5 5M3.5 6v6h7V6M6 12V9h2v3"/></svg>Buildings</li>
      <li class="nav__item"><svg viewBox="0 0 14 14"><path d="M1 3h5v9H1zM8 3h5v9H8z"/></svg>Contractors Address Book</li>
      <li class="nav__item"><svg viewBox="0 0 14 14"><path d="M3 1h8v12H3zM5 4h4M5 7h4M5 10h2"/></svg>Report Builder</li>
      <li class="nav__item"><svg viewBox="0 0 14 14"><ellipse cx="7" cy="3" rx="5" ry="2"/><path d="M2 3v8c0 1 2 2 5 2s5-1 5-2V3M2 7c0 1 2 2 5 2s5-1 5-2"/></svg>Management Data</li>
      <li class="nav__item"><svg viewBox="0 0 14 14"><path d="M1 3h12v9H1zM1 3l6 5 6-5"/></svg>Email Log Report</li>
      <li class="nav__item"><svg viewBox="0 0 14 14"><ellipse cx="7" cy="3" rx="5" ry="2"/><path d="M2 3v8c0 1 2 2 5 2s5-1 5-2V3"/></svg>&nbsp;&nbsp;&nbsp;Administration<svg class="nav__chev" viewBox="0 0 14 14"><path d="M3 5l4 4 4-4"/></svg></li>
      <li class="nav__item"><svg viewBox="0 0 14 14"><circle cx="6" cy="4" r="2.5"/><path d="M1 13c0-3 2-5 5-5M9 10l1.5 1.5L13 9"/></svg>About Us + Support</li>
      <li class="nav__item"><svg viewBox="0 0 14 14"><path d="M1 3h5v9H1zM8 3h5v9H8z"/></svg>Training Hub</li>
    </ul>
  </aside>

  <main class="main">
    <header class="topbar">
      <h2 class="topbar__title">Dashboard</h2>
      <div class="theme">
        <svg viewBox="0 0 14 14"><circle cx="7" cy="7" r="2.5"/><path d="M7 1v2M7 11v2M1 7h2M11 7h2M2.8 2.8l1.4 1.4M9.8 9.8l1.4 1.4M2.8 11.2l1.4-1.4M9.8 4.2l1.4-1.4"/></svg>
        <span class="toggle"></span>
        <svg viewBox="0 0 14 14"><path d="M11 9A5 5 0 0 1 5 3a5 5 0 1 0 6 6z"/></svg>
      </div>
      <span class="company">USER COMPANY LOGO</span>
      <span class="company-badge">LO<br>GO</span>
    </header>

    <div class="userbar">
      <span class="gear"><svg viewBox="0 0 12 12"><circle cx="6" cy="6" r="2"/><circle cx="6" cy="6" r="4.5" stroke-dasharray="2 1.5"/></svg></span>
      <span class="avatar" role="img" aria-label="User profile photo"></span>
      <div><div class="user__name">PELVORN</div><div class="user__mail">admininfo@postmail.com</div></div>
      <div class="user__icons">
        <svg viewBox="0 0 14 14"><path d="M3 10V6a4 4 0 0 1 8 0v4l1 1H2zM6 13h2"/></svg>
        <svg viewBox="0 0 14 14"><path d="M1 3h12v8H1zM1 3l6 5 6-5"/></svg>
      </div>
    </div>

    <div class="stats">
      <div class="stat stat--portfolio"><span class="stat__num">8</span><span class="stat__label">Building in This<br>Portfolio</span><svg class="stat__icon" viewBox="0 0 32 32"><path d="M4 30V10h10v20M14 30V4h12v26M2 30h28M7 14h4M7 18h4M7 22h4M17 8h6M17 12h6M17 16h6M17 20h6M17 24h6"/></svg></div>
      <div class="stat stat--actions"><span class="stat__num">10</span><span class="stat__label">Today's Next<br>Actions</span><svg class="stat__icon" viewBox="0 0 32 32"><path d="M24 18v10H4V10h8M20 4h8v8M28 4 16 16"/></svg></div>
      <div class="stat stat--inspections"><span class="stat__num">10</span><span class="stat__label stat__label--small">Upcoming<br>Inspections/ Expiring<br>Contracts</span><svg class="stat__icon" viewBox="0 0 32 32"><path d="M3 6h26v22H3zM3 12h26M9 3v6M23 3v6M8 17h3M14 17h3M20 17h3M8 22h3M14 22h3M20 22h3"/></svg></div>
      <div class="calendar">
        <div class="calendar__head"><span>Select Your Date &amp; Time</span><i></i></div>
        <div class="calendar__month">‹&nbsp;&nbsp;September 2025&nbsp;&nbsp;›</div>
        <div class="calendar__grid">
          <b>SUN</b><b>MON</b><b>TUE</b><b>WED</b><b>THU</b><b>FRI</b><b>SAT</b>
          <span>28</span><span>29</span><span>30</span><span>1</span><span>2</span><span>3</span><span>4</span>
          <span>5</span><span>6</span><span>7</span><span>8</span><span>9</span><span>10</span><span>11</span>
          <span>12</span><span>13</span><span>14</span><span>15</span><span>16</span><span>17</span><span>18</span>
          <span>19</span><span>20</span><span class="today">21</span><span>22</span><span>23</span><span>24</span><span>25</span>
          <span>26</span><span>27</span><span>28</span><span>29</span><span>30</span><span>31</span><span>1</span>
        </div>
      </div>
      <div class="stat stat--insurance"><span class="stat__num">10</span><span class="stat__label">Insurance Pending<br>or Overview</span><svg class="stat__icon" viewBox="0 0 32 32"><path d="M3 16a13 13 0 0 1 26 0zM16 16v10a3 3 0 0 1-6 0M16 3v2"/></svg></div>
      <div class="stat stat--defects"><span class="stat__num">10</span><span class="stat__label stat__label--small">Defects Register\<br>Feedback Requested</span><svg class="stat__icon" viewBox="0 0 32 32"><path d="M24 16v12H4V6h14M8 12h8M8 17h8M8 22h6M28 6 18 18l-3 1 1-3L26 4z"/></svg></div>
      <div class="stat stat--maintenance"><span class="stat__num">8</span><span class="stat__label">Open Maintenance<br>Requests</span><svg class="stat__icon" viewBox="0 0 32 32"><circle cx="18" cy="11" r="4"/><circle cx="18" cy="11" r="8" stroke-dasharray="3 2"/><path d="M2 24h6l6 3 10-4M8 24l5-4h5"/></svg></div>
    </div>

    <div class="row-two">
      <div class="chart">
        <h3 class="chart__title">Overview</h3>
        <span class="chart__range">This Month</span>
        <svg viewBox="0 0 400 185" font-family="Poppins" font-size="7" fill="#555">
          <defs><linearGradient id="areaFill" x1="0" y1="0" x2="0" y2="1"><stop offset="0" stop-color="#a58bf0" stop-opacity=".75"/><stop offset="1" stop-color="#c9b8f6" stop-opacity=".45"/></linearGradient></defs>
          <g stroke="#e4e1ee" stroke-width=".6">
            <path d="M20 10h370M20 40h370M20 70h370M20 100h370M20 130h370M20 160h370"/>
            <path d="M40 10v150M70 10v150M100 10v150M130 10v150M160 10v150M190 10v150M220 10v150M250 10v150M280 10v150M310 10v150M340 10v150M370 10v150"/>
          </g>
          <text x="2" y="13">100</text><text x="6" y="43">80</text><text x="6" y="73">60</text><text x="6" y="103">40</text><text x="6" y="133">20</text><text x="10" y="163">0</text>
          <path d="M24 52 C34 44 44 39 66 37 S90 35 96 36 S116 38 120 42 S140 80 150 90 S162 160 176 158 S190 80 203 73 S222 66 232 66 S250 90 258 90 S276 62 288 62 S310 90 318 101 S345 112 355 120 S372 130 380 131 L380 160 L24 160 Z" fill="url(#areaFill)"/>
          <path d="M24 52 C34 44 44 39 66 37 S90 35 96 36 S116 38 120 42 S140 80 150 90 S162 160 176 158 S190 80 203 73 S222 66 232 66 S250 90 258 90 S276 62 288 62 S310 90 318 101 S345 112 355 120 S372 130 380 131" fill="none" stroke="#8f74e6" stroke-width="1.5"/>
          <g fill="#fff" stroke="#8f74e6" stroke-width="1"><circle cx="66" cy="37" r="2"/><circle cx="96" cy="36" r="2"/><circle cx="150" cy="90" r="2"/><circle cx="176" cy="158" r="2"/><circle cx="203" cy="73" r="2"/><circle cx="232" cy="66" r="2"/><circle cx="258" cy="90" r="2"/><circle cx="318" cy="101" r="2"/><circle cx="355" cy="120" r="2"/><circle cx="380" cy="131" r="2"/></g>
          <text x="196" y="172">April</text>
        </svg>
      </div>
      <div class="actions">
        <div class="actions__title"><svg viewBox="0 0 14 14"><path d="M12 7v6H1V2h8M4 6l3 3 6-7"/></svg>Next Action List</div>
        <div class="select">Pelvorn</div>
        <div class="action-list">
          <div class="action__date">22 August, 2025</div><p class="action__text">Streamline building engagement. Immediate access to data. New Buildings.</p>
          <div class="action__date">25 August, 2025</div><p class="action__text">Streamline building engagement. Immediate access to data. New Buildings.</p>
          <div class="action__date">27 August, 2025</div><p class="action__text">Streamline building engagement. Immediate access to data. New Buildings.</p>
        </div>
        <span class="btn-more">More</span>
      </div>
    </div>

    <section class="filter">
      <div class="filter__head">
        <h3 class="filter__title">Buildings Filter</h3>
        <span class="btn btn--primary">+Add New</span>
        <span class="btn btn--outline">Export to Excel</span>
        <span class="collapse"></span>
      </div>
      <div class="filter__body">
        <div class="field"><label>Units Plan No.</label><div class="input">Units Plan No.</div></div>
        <div class="field"><label>Building Name</label><div class="input">Building name</div></div>
        <div class="field"><label>Street Name</label><div class="input">Street name</div></div>
        <div class="field"><label>Street No.</label><div class="input">Street No.</div></div>
        <div class="field"><label>Suburb</label><div class="select">Select--</div></div>
        <div class="field"><label>Group</label><div class="select">Select--</div></div>
        <div class="field"><label>Builder</label><div class="input">Builder</div></div>
        <div class="field"><label>Building Status</label><div class="select">Active</div></div>
      </div>
    </section>

    <section class="buildings">
      <table>
        <colgroup><col style="width:45px"><col style="width:76px"><col style="width:79px"><col style="width:72px"><col style="width:79px"><col style="width:52px"><col style="width:55px"><col style="width:111px"><col></colgroup>
        <thead><tr><th class="c">S.No.</th><th>Units Plan No.</th><th>Building Name</th><th>Group Name</th><th class="c">Street<br>Number &amp; Name</th><th>Suburb</th><th>Live Posts</th><th class="c">Pelvorn Subscriptions<br>Renewal</th><th class="c">Action</th></tr></thead>
        <tbody>
          <tr><td>01.</td><td>000884</td><td>Building Name</td><td>Harlow Brennan</td><td>41 Tallow Street</td><td>Merridale</td><td>00</td><td class="num">09-May-2026</td><td class="act"><i class="ic e"></i><i class="ic c"></i><i class="ic x"></i></td></tr>
          <tr><td>02.</td><td>000884</td><td>Building Name</td><td>Harlow Brennan</td><td>41 Tallow Street</td><td>Merridale</td><td>00</td><td class="num">09-May-2026</td><td class="act"><i class="ic e"></i><i class="ic c"></i><i class="ic x"></i></td></tr>
          <tr><td>03.</td><td>000884</td><td>Building Name</td><td>Harlow Brennan</td><td>41 Tallow Street</td><td>Merridale</td><td>00</td><td class="num">09-May-2026</td><td class="act"><i class="ic e"></i><i class="ic c"></i><i class="ic x"></i></td></tr>
          <tr><td>04.</td><td>000884</td><td>Building Name</td><td>Harlow Brennan</td><td>41 Tallow Street</td><td>Merridale</td><td>00</td><td class="num">09-May-2026</td><td class="act"><i class="ic e"></i><i class="ic c"></i><i class="ic x"></i></td></tr>
          <tr><td>05.</td><td>000884</td><td>Building Name</td><td>Harlow Brennan</td><td>41 Tallow Street</td><td>Merridale</td><td>00</td><td class="num">09-May-2026</td><td class="act"><i class="ic e"></i><i class="ic c"></i><i class="ic x"></i></td></tr>
          <tr><td>06.</td><td>000884</td><td>Building Name</td><td>Harlow Brennan</td><td>41 Tallow Street</td><td>Merridale</td><td>00</td><td class="num">09-May-2026</td><td class="act"><i class="ic e"></i><i class="ic c"></i><i class="ic x"></i></td></tr>
          <tr><td>07.</td><td>000884</td><td>Building Name</td><td>Harlow Brennan</td><td>41 Tallow Street</td><td>Merridale</td><td>00</td><td class="num">09-May-2026</td><td class="act"><i class="ic e"></i><i class="ic c"></i><i class="ic x"></i></td></tr>
          <tr><td>08.</td><td>000884</td><td>Building Name</td><td>Harlow Brennan</td><td>41 Tallow Street</td><td>Merridale</td><td>00</td><td class="num">09-May-2026</td><td class="act"><i class="ic e"></i><i class="ic c"></i><i class="ic x"></i></td></tr>
          <tr><td>09.</td><td>000884</td><td>Building Name</td><td>Harlow Brennan</td><td>41 Tallow Street</td><td>Merridale</td><td>00</td><td class="num">09-May-2026</td><td class="act"><i class="ic e"></i><i class="ic c"></i><i class="ic x"></i></td></tr>
          <tr><td>10.</td><td>000884</td><td>Building Name</td><td>Harlow Brennan</td><td>41 Tallow Street</td><td>Merridale</td><td>00</td><td class="num">09-May-2026</td><td class="act"><i class="ic e"></i><i class="ic c"></i><i class="ic x"></i></td></tr>
          <tr><td>11.</td><td>000884</td><td>Building Name</td><td>Harlow Brennan</td><td>41 Tallow Street</td><td>Merridale</td><td>00</td><td class="num">09-May-2026</td><td class="act"><i class="ic e"></i><i class="ic c"></i><i class="ic x"></i></td></tr>
          <tr><td>12.</td><td>000884</td><td>Building Name</td><td>Harlow Brennan</td><td>41 Tallow Street</td><td>Merridale</td><td>00</td><td class="num">09-May-2026</td><td class="act"><i class="ic e"></i><i class="ic c"></i><i class="ic x"></i></td></tr>
          <tr><td>13</td><td>000884</td><td>Building Name</td><td>Harlow Brennan</td><td>41 Tallow Street</td><td>Merridale</td><td>00</td><td class="num">09-May-2026</td><td class="act"><i class="ic e"></i><i class="ic c"></i><i class="ic x"></i></td></tr>
          <tr><td>14.</td><td>000884</td><td>Building Name</td><td>Harlow Brennan</td><td>41 Tallow Street</td><td>Merridale</td><td>00</td><td class="num">09-May-2026</td><td class="act"><i class="ic e"></i><i class="ic c"></i><i class="ic x"></i></td></tr>
          <tr><td>15.</td><td>000884</td><td>Building Name</td><td>Harlow Brennan</td><td>41 Tallow Street</td><td>Merridale</td><td>00</td><td class="num">09-May-2026</td><td class="act"><i class="ic e"></i><i class="ic c"></i><i class="ic x"></i></td></tr>
          <tr><td>16.</td><td>000884</td><td>Building Name</td><td>Harlow Brennan</td><td>41 Tallow Street</td><td>Merridale</td><td>00</td><td class="num">09-May-2026</td><td class="act"><i class="ic e"></i><i class="ic c"></i><i class="ic x"></i></td></tr>
          <tr><td>17.</td><td>000884</td><td>Building Name</td><td>Harlow Brennan</td><td>41 Tallow Street</td><td>Merridale</td><td>00</td><td class="num">09-May-2026</td><td class="act"><i class="ic e"></i><i class="ic c"></i><i class="ic x"></i></td></tr>
          <tr><td>18.</td><td>000884</td><td>Building Name</td><td>Harlow Brennan</td><td>41 Tallow Street</td><td>Merridale</td><td>00</td><td class="num">09-May-2026</td><td class="act"><i class="ic e"></i><i class="ic c"></i><i class="ic x"></i></td></tr>
          <tr><td>19.</td><td>000884</td><td>Building Name</td><td>Harlow Brennan</td><td>41 Tallow Street</td><td>Merridale</td><td>00</td><td class="num">09-May-2026</td><td class="act"><i class="ic e"></i><i class="ic c"></i><i class="ic x"></i></td></tr>
          <tr><td>20.</td><td>000884</td><td>Building Name</td><td>Harlow Brennan</td><td>41 Tallow Street</td><td>Merridale</td><td>00</td><td class="num">09-May-2026</td><td class="act"><i class="ic e"></i><i class="ic c"></i><i class="ic x"></i></td></tr>
        </tbody>
      </table>
      <div class="pager">
        <span class="pager__btn pager__btn--off">‹&nbsp; Back</span><span class="pager__page">1</span><span class="pager__btn">Next &nbsp;›</span>
        <span class="pager__label">Result per page</span><span class="pager__size">20 <small>⌄</small></span><span class="pager__count">1-20 of 100</span>
      </div>
    </section>
  </main>

  <footer class="footer">Copyright © 2025 Pelvorn | All Rights Reserved | Privacy Policy</footer>
</section>

</body>
</html>
```